Jewellery Shop of 20 over years needs a new Business Card

We need a new business card that is refreshing, trendy for our Jewellery shop. We carry mid to high end fine jewellery. We want the design of the new business card to be clean cut, refreshing and different. Please try to keep to using the same logo we have, and for more information on the company you can check us out on www.tolvarjewels.com.sg or on https://www.facebook.com/Tolvarjewelworks/

Target Market(s)

late 20s to 50s

Industry/Entity Type

Jewelry Store

Contact Information for Business Card

Tolvar's Jewel Works Co Pte Ltd
517 Kestrel Avenue, #02-14/15 Marwick Plaza Singapore 249913
Tel: (65) 64721958 Fax:( 65) 64721947 WhatsApp: ( 65) 90364158
Email: tolvarhoe@quillnet.com.sg
Website: www.tolvarjewels.com.sg

Tolvar Hoe
Gemologist/Designer/Founder since 1980

Font styles to use
Serif

Requirements
Must have
• Trendy, Classic Clean Look
Should not have
• Should not be too dull or old looking, should not look like my old business card, no photos of jewellery

```html
<!DOCTYPE html>
<html lang="en">
<head>
<meta charset="utf-8">
<title>Tolvar's Jewel Works – Business Card</title>
<link rel="stylesheet" href="https://fonts.googleapis.com/css2?family=Cormorant+Garamond:wght@500;600;700&display=swap">
<style>
  :root {
    --olive: #383a1b;
    --olive-deep: #2f3116;
    --gold: #c8a24f;
    --gold-soft: #d9b868;
    --paper: #ffffff;
    --ink: #2a2a22;
    --stage: #e9e5dc;
  }
  * { box-sizing: border-box; margin: 0; padding: 0; }
  html, body { width: 1200px; height: 913px; overflow: hidden; }
  body {
    background: var(--stage);
    font-family: "Cormorant Garamond", Georgia, serif;
    position: relative;
  }
  .card {
    position: absolute;
    width: 560px;
    height: 320px;
    box-shadow: 0 10px 28px rgba(0,0,0,.22);
    overflow: hidden;
  }

  /* Front */
  .card-front {
    left: 70px; top: 80px;
    background: var(--olive);
    color: var(--gold);
    display: flex; flex-direction: column; align-items: center; justify-content: center;
    text-align: center;
  }
  .brand-mark {
    display: flex; flex-direction: column; align-items: center; gap: 14px;
  }
  .brand-dot {
    width: 54px; height: 54px; border-radius: 50%;
    border: 2px solid var(--gold);
  }
  .brand-name { font-size: 38px; font-weight: 600; letter-spacing: .5px; }
  .front-tagline { margin-top: 12px; font-size: 19px; font-weight: 500; }
  .front-specialty { margin-top: 6px; font-size: 17px; font-weight: 500; }

  /* Back */
  .card-back {
    left: 570px; top: 510px;
    background: var(--paper);
  }
  .back-panel {
    position: absolute; left: 0; top: 0; bottom: 0; width: 215px;
    background: var(--olive);
    color: var(--gold);
    display: flex; flex-direction: column; align-items: center; justify-content: center;
    text-align: center; padding: 0 14px;
  }
  .back-panel .brand-dot { width: 40px; height: 40px; }
  .back-panel .brand-name { font-size: 24px; line-height: 1.1; }
  .address { margin-top: 22px; font-size: 16px; line-height: 1.35; font-weight: 500; }

  .accent-bar {
    position: absolute; left: 215px; top: 0; width: 14px; height: 118px;
    background: var(--gold);
  }
  .accent-foot {
    position: absolute; left: 215px; top: 118px; width: 36px; height: 3px;
    background: var(--gold);
  }
  .contact {
    position: absolute; right: 26px; top: 18px; left: 250px;
    text-align: right;
  }
  .company-line { font-size: 15px; color: var(--gold); font-weight: 500; }
  .person-name {
    font-size: 30px; color: var(--gold); font-weight: 700; letter-spacing: 1.5px;
    text-transform: uppercase; line-height: 1.05;
  }
  .person-role { font-size: 14px; color: var(--ink); font-weight: 600; }
  .contact-list { list-style: none; margin-top: 8px; }
  .contact-list li {
    display: flex; justify-content: flex-end; align-items: center; gap: 8px;
    font-size: 17px; color: var(--ink); font-weight: 600; line-height: 1.3;
  }
  .icon-badge {
    width: 16px; height: 16px; border-radius: 50%; background: var(--gold);
    display: inline-flex; align-items: center; justify-content: center; flex: none;
  }
  .icon-badge svg { width: 10px; height: 10px; fill: #fff; }
  .email-line {
    position: absolute; right: 26px; top: 218px;
    font-size: 17px; color: var(--ink); font-weight: 600;
  }
  .web-band {
    position: absolute; left: 215px; right: 0; top: 250px; height: 40px;
    background: var(--gold);
    display: flex; align-items: center; gap: 12px; padding-left: 22px;
    color: var(--olive-deep); font-size: 20px; font-weight: 700;
  }
  .web-band .globe { width: 18px; height: 18px; }
</style>
</head>
<body>

<section class="card card-front" aria-label="Business card front">
  <div class="brand-mark">
    <span class="brand-dot"></span>
    <span class="brand-name">Tolvar's Jewel Works</span>
  </div>
  <p class="front-tagline">Bespoke Jewellery</p>
  <p class="front-specialty">Specialising in VGL Certified Diamond &amp; Precious Stone Since 1993</p>
</section>

<section class="card card-back" aria-label="Business card back">
  <div class="back-panel">
    <div class="brand-mark">
      <span class="brand-dot"></span>
      <span class="brand-name">Tolvar's Jewel Works</span>
    </div>
    <p class="address">517 Kestrel Avenue<br>#02-14/15 Marwick Plaza<br>Singapore 249913</p>
  </div>

  <span class="accent-bar"></span>
  <span class="accent-foot"></span>

  <div class="contact">
    <p class="company-line">Tolvar's Jewel Works Co Pte Ltd</p>
    <p class="person-name">Tolvar Hoe</p>
    <p class="person-role">Gemologist/Designer/Founder since 1980</p>
    <ul class="contact-list">
      <li>(65) 64721958
        <span class="icon-badge"><svg viewBox="0 0 10 10"><path d="M2 1l2 2-1 1c.6 1.2 1.6 2.2 2.8 2.8l1-1 2 2-1.3 1.3C4.6 9 1 5.4.7 2.3z"/></svg></span>
      </li>
      <li>(65) 64721947
        <span class="icon-badge"><svg viewBox="0 0 10 10"><rect x="2.5" y="1" width="5" height="3"/><rect x="1" y="4" width="8" height="3.5" rx=".5"/><rect x="2.5" y="7" width="5" height="2"/></svg></span>
      </li>
      <li>(65) 90364158
        <span class="icon-badge"><svg viewBox="0 0 10 10"><path d="M5 1a4 4 0 0 0-3.4 6.1L1 9l2-.6A4 4 0 1 0 5 1z"/></svg></span>
      </li>
    </ul>
  </div>

  <p class="email-line">tolvarhoe@quillnet.com.sg
    <span class="icon-badge" style="vertical-align:middle;margin-left:6px"><svg viewBox="0 0 10 10"><path d="M1 2.5h8v5H1z M1 2.5l4 3 4-3" fill="none" stroke="#fff" stroke-width="1"/></svg></span>
  </p>

  <div class="web-band">
    <svg class="globe" viewBox="0 0 18 18"><circle cx="9" cy="9" r="8" fill="var(--olive-deep)"/><path d="M1 9h16M9 1c-3 3-3 13 0 16M9 1c3 3 3 13 0 16" fill="none" stroke="var(--gold)" stroke-width="1"/></svg>
    <span>www.tolvarjewels.com.sg</span>
  </div>
</section>

</body>
</html>
```